TallFernSix needs some a graphic design ASAP. Visit https://tallfernsix.com/Home/About/ to get a feel for our current design. We need a visually pleasing way to add the information in the files attached to what already exists (the new sections are Reach, Discretion, and Heart).

This can either be a graphic with the information at the bottom or a redesign of the landing page. We'll accept whatever we like most.

I've attached some stock photos that I own / like. Feel free to use these directly or for inspiration. Icons are OK too. These are just an example.

```html
<!DOCTYPE html>
<html lang="en">
<head>
<meta charset="utf-8">
<title>TallFernSix — Discretion, Reach, Heart</title>
<link rel="stylesheet" href="https://fonts.googleapis.com/css2?family=Open+Sans:wght@400;700&display=swap">
<style>
  :root {
    --page-bg: #ffffff;
    --card-bg: #ffffff;
    --card-border: #e2e2e2;
    --header-top: #ffffff;
    --header-bottom: #efefef;
    --title-ink: #111111;
    --body-ink: #1a1a1a;
    --brand-blue: #29bdf0;
    --brand-pink: #f21f7c;
  }
  * { box-sizing: border-box; margin: 0; padding: 0; }
  html, body {
    width: 1200px;
    height: 707px;
    overflow: hidden;
    background: var(--page-bg);
    font-family: "Open Sans", Arial, sans-serif;
  }
  .features {
    position: absolute;
    top: 195px;
    left: 89px;
    display: flex;
    gap: 21px;
  }
  .feature-card {
    width: 327px;
    height: 304px;
    background: var(--card-bg);
    border: 1px solid var(--card-border);
    border-radius: 5px;
    overflow: hidden;
    display: flex;
    flex-direction: column;
  }
  .feature-title {
    height: 56px;
    padding: 0 26px;
    display: flex;
    align-items: center;
    background: linear-gradient(var(--header-top), var(--header-bottom));
    border-bottom: 1px solid var(--card-border);
    font-size: 20px;
    font-weight: 700;
    color: var(--title-ink);
    letter-spacing: 0.2px;
  }
  .feature-icon {
    width: 128px;
    height: 112px;
    margin: 28px auto 0;
    border-radius: 10px;
  }
  .icon-discretion { background: linear-gradient(135deg, var(--brand-blue) 60%, var(--brand-pink)); }
  .icon-reach { background: linear-gradient(180deg, var(--brand-blue) 40%, var(--brand-pink)); }
  .icon-heart { background: linear-gradient(0deg, var(--brand-blue) 50%, var(--brand-pink)); }
  .feature-text {
    margin-top: 22px;
    padding: 0 14px;
    text-align: center;
    font-size: 16px;
    line-height: 20.5px;
    color: var(--body-ink);
  }
</style>
</head>
<body>
  <section class="features">
    <article class="feature-card">
      <h2 class="feature-title">DISCRETION</h2>
      <div class="feature-icon icon-discretion" role="img" aria-label="Icon of a private profile document with a heart award ribbon"></div>
      <p class="feature-text">Register with a private profile<br>and reveal yourself only to<br>matchmakers you choose.</p>
    </article>
    <article class="feature-card">
      <h2 class="feature-title">REACH</h2>
      <div class="feature-icon icon-reach" role="img" aria-label="Icon of three people connected by circling arrows"></div>
      <p class="feature-text">Human matchmakers have friends,<br>family, co-workers and acquaintances.<br>When has an algorithm<br>set you up with its cousin?</p>
    </article>
    <article class="feature-card">
      <h2 class="feature-title">HEART</h2>
      <div class="feature-icon icon-heart" role="img" aria-label="Icon of two open hands holding a heart"></div>
      <p class="feature-text">If no matchmakers succeed in finding<br>you a match, your reward<br>will be donated<br>to a charity of your choice.</p>
    </article>
  </section>
</body>
</html>
```